Letterhead Design

We need a new Letterhead design for a 30 year old Electrical Company. We service domestic and commercial places. We have a logo recently made so to incorporate that. Using same colours or interested to see others added.
Would like to see a couple of options with all the info in letterhead, then another with info in a footnote down the bottom.

info needed to be added:

-Lic. No 48162
8/22-24 Larkin Rd, Tolvern 2087
W - brightcoilpower.com.au
T - (02) 9471 3825
M - 0427 593 168
E - info@brightcoilpower.com.au
ABN: 42 597 214 630

Electrical

```html
<!DOCTYPE html>
<html lang="en">
<head>
<meta charset="utf-8">
<title>Brightcoil Power Electrical – Letterhead</title>
<link rel="stylesheet" href="https://fonts.googleapis.com/css2?family=Tinos:ital,wght@0,400;1,700&display=swap">
<style>
  :root {
    --brand-orange: #ff6a13;
    --brand-black: #000000;
    --paper: #ffffff;
    --ink: #222222;
    --type-serif: "Tinos", "Times New Roman", serif;
  }
  html, body {
    margin: 0;
    padding: 0;
    width: 1200px;
    height: 851px;
    overflow: hidden;
    background: var(--paper);
  }
  .letterhead {
    display: block;
    width: 1200px;
    height: 851px;
  }
  .header-band { fill: var(--brand-black); stroke: var(--brand-orange); stroke-width: 12; }
  .frame-line { fill: none; stroke: var(--brand-orange); stroke-width: 8; }
  .frame-dot { fill: var(--brand-orange); }
  .tagline-rule { stroke: var(--brand-orange); stroke-width: 3; }
  .brand-name {
    font-family: var(--type-serif);
    font-weight: 400;
    font-size: 64px;
    fill: var(--paper);
  }
  .brand-dot { fill: var(--brand-orange); }
  .intro {
    font-family: var(--type-serif);
    font-style: italic;
    font-weight: 700;
    font-size: 32px;
    fill: var(--ink);
  }
  .contact {
    font-family: var(--type-serif);
    font-style: italic;
    font-weight: 700;
    font-size: 20px;
    fill: var(--ink);
  }
</style>
</head>
<body>
<svg class="letterhead" viewBox="0 0 1200 851" xmlns="http://www.w3.org/2000/svg">
  <!-- Header band with company name -->
  <rect class="header-band" x="45" y="55" width="1106" height="277"/>
  <circle class="brand-dot" cx="330" cy="178" r="16"/>
  <text class="brand-name" x="620" y="200" text-anchor="middle">Brightcoil Power</text>

  <!-- Frame lines running down from the header -->
  <polyline class="frame-line" points="121,336 121,652 202,652 202,736"/>
  <circle class="frame-dot" cx="202" cy="738" r="13"/>
  <polyline class="frame-line" points="1072,336 1072,652 990,652 990,734"/>
  <circle class="frame-dot" cx="990" cy="736" r="13"/>

  <!-- Introduction -->
  <g class="intro" text-anchor="middle">
    <text x="584" y="395">We are a 30 year old Electrical Company,who service</text>
    <text x="584" y="457">domestic and commercial places. We look forward</text>
    <text x="584" y="521">to working with you in whatever capicity we can,</text>
    <text x="570" y="577">Brightcoil Power Electrical are well equipped &amp;</text>
    <text x="603" y="633">competent in taking on new enterprises.</text>
  </g>
  <line class="tagline-rule" x1="270" y1="647" x2="922" y2="647"/>

  <!-- Contact details -->
  <g class="contact">
    <text x="238" y="680">Lic. No 48162</text>
    <text x="235" y="711">8/22-24 Larkin Rd, Tolvern 2087</text>
    <text x="233" y="745">W - brightcoilpower.com.au</text>
    <text x="231" y="773">T - (02) 9471 3825</text>
    <text x="656" y="677">M - 0427 593 168</text>
    <text x="656" y="709">E - info@brightcoilpower.com.au</text>
    <text x="656" y="748">ABN: 42 597 214 630</text>
  </g>
</svg>
</body>
</html>
```